College Social website needs a SIMPLE chart design

We need a simple one page website. The website is called "Fim-Bosk" a phonetic spelling of the word collage. The site allows users to gain up to date information on the nightlife and social scene of the campus. The site must be able to easily convey several key pieces of information; some type of grid/chart would work well.

This includes:
primary information:
-The name of the bar (about 9 bars on campus)
-The length of the line
-Guy/Girl ratio
-If there is cover (admittance fee) to enter the bar

secondary information:
-how packed/full the bar is
-if there is police raiding the bar
-a way to show more information including drink specials

would prefer a design similar to this page except more colorful/playful/fun: http://m.vantorelq.com/results.php

Some stylistic tips - the name of the service is called fim bosk. a phonetic spelling of collage (http://en.quorbinet.org/wiki/Collage). it doesnt need to look like a rainbow, just be exciting, engaging, and vivid.

look at this page for reference: http://www.plimvadee.com/blog/flat-ui-design-showcase/

other than the bar name and drink specials, everything should be presented graphically. All the bar stats are approximations and rough estimates, so you must find a way to present the information as relatives. historical information is not relevant. only the real time stats need to be included. here is a sample:

Bar name: Sample bar
guy/girl ratio: 70/30
line length: short
admittance fee: yes
bar attendance: near full
police raid: no
drink specials:
WINE NIGHT!
$8 BOTTLES OF GALLOWMERE WINE
$8 BOTTLES OF CHAMPAGNE
$2 TRESK PALE BOTTLES
$2 WELLS

Target Market(s)

target market for the site is 18-21 year olds in college.

Industry/Entity Type

College

Requirements
Must have
• the design MUST be mobile friendly. keep it simple. a flat design would be preferred.
the information must be conveyed in the form of symbols/icons. for instance, a pie chart to show guy/girl ratio.

```html
<!DOCTYPE html>
<html lang="en">
<head>
<meta charset="utf-8">
<title>Fim-Bosk</title>
<link rel="stylesheet" href="https://fonts.googleapis.com/css2?family=Alegreya+Sans:wght@400;500;700;800&family=Arimo:wght@400;700&display=swap">
<style>
  :root{
    --ink:#111111;
    --charcoal:#262626;
    --panel:#2a2a2a;
    --deep:#1a1a1a;
    --red:#c8141b;
    --paper:#ffffff;
  }
  *{box-sizing:border-box;margin:0;padding:0}
  html,body{width:864px;height:1200px;overflow:hidden;background:var(--deep)}
  body{font-family:"Alegreya Sans",sans-serif;color:var(--paper);position:relative}
  .site-header{position:absolute;left:0;top:0;width:864px;height:64px;background:var(--charcoal);display:flex;align-items:center;justify-content:center}
  .brand{font-size:34px;font-weight:700;letter-spacing:-0.5px;color:var(--paper)}
  .filters-bar{position:absolute;left:0;top:66px;width:864px;height:34px;background:var(--red);font-family:"Arimo",sans-serif;font-size:19px;padding-left:29px;line-height:34px}
  .bar-detail{position:absolute;left:0;top:112px;width:864px;height:102px;background:var(--charcoal)}
  .stats{position:absolute;left:44px;top:16px;width:170px;font-size:8px;font-weight:700;line-height:11px}
  .stats-grid{display:grid;grid-template-columns:86px 84px}
  .stat{display:flex;align-items:center;gap:3px;height:11px}
  .stat svg{width:11px;height:10px;flex:none}
  .specials{text-align:center;margin-top:3px;line-height:9.5px;font-size:7px;text-transform:uppercase}
  .detail-divider{position:absolute;left:252px;top:20px;width:3px;height:68px;background:var(--paper)}
  .detail-name{position:absolute;left:264px;top:28px;font-size:36px;font-weight:700;color:var(--red);line-height:1}
  .contact-icons{position:absolute;left:622px;top:20px;width:24px}
  .contact-icons svg{display:block;width:22px;height:24px;margin-bottom:12px}
  .expand-icon{position:absolute;left:796px;top:38px;width:50px;height:50px}
  .bar-list{position:absolute;left:0;top:216px;width:864px;list-style:none}
  .bar-row{position:relative;height:105.3px;border-top:3px solid var(--ink);background:var(--panel)}
  .bar-row .row-shape{position:absolute;left:0;top:0;width:864px;height:102px}
  .map-icon{position:absolute;left:20px;top:22px;width:58px;height:58px}
  .bar-name{position:absolute;left:89px;top:28px;font-size:20px;font-weight:500;color:var(--ink);line-height:1}
  .bar-more{position:absolute;left:103px;top:52px;font-size:14px;font-weight:500;color:var(--red);line-height:1}
  .more-band{position:absolute;left:0;top:1057px;width:864px;height:56px;background:var(--deep)}
  .more-button{position:absolute;left:345px;top:9px;width:182px;height:28px;background:var(--charcoal);border-left:7px solid var(--red);border-right:7px solid var(--red);text-align:center;font-size:20px;font-weight:700;line-height:28px}
  .contact-band{position:absolute;left:0;top:1113px;width:864px;height:64px;background:var(--charcoal)}
  .contact-title{position:absolute;left:29px;top:18px;font-size:21px;font-weight:700}
  .social{position:absolute;top:18px;width:27px;height:27px;border-radius:50%;background:var(--paper)}
  .social-one{left:761px}
  .social-two{left:793px}
  .site-footer{position:absolute;left:0;top:1177px;width:864px;height:23px;background:var(--red)}
</style>
</head>
<body>
<svg width="0" height="0" style="position:absolute">
  <defs>
    <symbol id="row-shape" viewBox="0 0 864 102">
      <polygon points="0,0 790,0 756,102 0,102" fill="#ffffff"/>
      <polygon points="796,0 801,0 767,102 762,102" fill="#ffffff"/>
      <rect x="817" y="49" width="22" height="4" fill="#c8141b"/>
      <rect x="826" y="40" width="4" height="22" fill="#c8141b"/>
    </symbol>
    <symbol id="map-icon" viewBox="0 0 58 58">
      <polygon points="3,18 16,13 29,18 42,13 42,52 29,57 16,52 3,57" fill="none" stroke="#111" stroke-width="3" stroke-linejoin="round"/>
      <line x1="16" y1="13" x2="16" y2="52" stroke="#111" stroke-width="3"/>
      <line x1="29" y1="18" x2="29" y2="57" stroke="#111" stroke-width="3"/>
      <path d="M8,42 L14,36 L22,40 L30,33 L36,37" fill="none" stroke="#111" stroke-width="2" stroke-dasharray="3 2"/>
      <path d="M46,2 a8,8 0 0 1 8,8 c0,6 -8,14 -8,14 c0,0 -8,-8 -8,-14 a8,8 0 0 1 8,-8z" fill="#111"/>
      <circle cx="46" cy="10" r="3" fill="#fff"/>
    </symbol>
  </defs>
</svg>

<header class="site-header">
  <span class="brand">Fim-Bosk</span>
</header>

<div class="filters-bar">Filters</div>

<section class="bar-detail">
  <div class="stats">
    <div class="stats-grid">
      <div class="stat"><svg viewBox="0 0 11 10"><circle cx="3" cy="3" r="2" fill="none" stroke="#fff"/><line x1="3" y1="5" x2="3" y2="9" stroke="#fff"/><circle cx="8" cy="5" r="2" fill="none" stroke="#fff"/><line x1="9.5" y1="3.5" x2="11" y2="2" stroke="#fff"/></svg>: 70/30</div>
      <div class="stat"><svg viewBox="0 0 11 10"><rect x="2" y="1" width="7" height="8" rx="2" fill="none" stroke="#fff"/><circle cx="5.5" cy="4" r="1.5" fill="#fff"/></svg>: near full</div>
      <div class="stat"><svg viewBox="0 0 11 10"><line x1="0" y1="5" x2="11" y2="5" stroke="#fff" stroke-width="1.5"/></svg>: short</div>
      <div class="stat"><svg viewBox="0 0 11 10"><circle cx="5.5" cy="4" r="3" fill="none" stroke="#fff"/><rect x="3" y="7" width="5" height="2" fill="#fff"/></svg>: no</div>
      <div class="stat"><svg viewBox="0 0 11 10"><circle cx="5.5" cy="5" r="4.5" fill="none" stroke="#fff"/><text x="5.5" y="7.5" font-size="7" text-anchor="middle" fill="#fff" font-family="Arimo,sans-serif">$</text></svg>: Yes</div>
      <div class="stat"><svg viewBox="0 0 11 10"><rect x="3" y="0" width="5" height="10" rx="2" fill="none" stroke="#fff"/></svg>: WINE NIGHT!</div>
    </div>
    <div class="specials">
      <p>Bottles of Gallowmere wine $8</p>
      <p>Bottles of champagne $8</p>
      <p>Tresk Pale bottles $2</p>
      <p>Wells $2</p>
    </div>
  </div>
  <div class="detail-divider"></div>
  <h1 class="detail-name">The name of the bar</h1>
  <div class="contact-icons">
    <svg viewBox="0 0 22 24" aria-label="Call"><path d="M5,2 L9,2 L10,7 L7,9 C8,13 10,16 13,18 L15,15 L20,17 L20,21 C20,22 19,23 18,23 C10,22 3,14 3,4 C3,3 4,2 5,2z" fill="#fff"/></svg>
    <svg viewBox="0 0 22 24" aria-label="Location"><path d="M11,22 C11,22 3,14 3,9 a8,8 0 0 1 16,0 c0,5 -8,13 -8,13z" fill="none" stroke="#fff" stroke-width="2.5"/></svg>
  </div>
  <svg class="expand-icon" viewBox="0 0 50 50" aria-label="Show more">
    <rect x="2" y="11" width="20" height="5" fill="#fff"/>
    <rect x="9.5" y="3.5" width="5" height="20" fill="#fff"/>
    <path d="M27,18 a2.5,2.5 0 0 1 5,0 v10 a2.5,2.5 0 0 1 5,0 v2 a2.5,2.5 0 0 1 5,0 v2 a2.5,2.5 0 0 1 5,0 v8 c0,5 -3,8 -8,8 h-6 c-3,0 -5,-2 -7,-5 l-6,-9 a2.5,2.5 0 0 1 4,-3 l3,4z" fill="#fff" stroke="#262626" stroke-width="1"/>
  </svg>
</section>

<ul class="bar-list">
  <li class="bar-row"><svg class="row-shape"><use href="#row-shape"/></svg><svg class="map-icon"><use href="#map-icon"/></svg><h2 class="bar-name">The name of the bar</h2><p class="bar-more">More details goes here</p></li>
  <li class="bar-row"><svg class="row-shape"><use href="#row-shape"/></svg><svg class="map-icon"><use href="#map-icon"/></svg><h2 class="bar-name">The name of the bar</h2><p class="bar-more">More details goes here</p></li>
  <li class="bar-row"><svg class="row-shape"><use href="#row-shape"/></svg><svg class="map-icon"><use href="#map-icon"/></svg><h2 class="bar-name">The name of the bar</h2><p class="bar-more">More details goes here</p></li>
  <li class="bar-row"><svg class="row-shape"><use href="#row-shape"/></svg><svg class="map-icon"><use href="#map-icon"/></svg><h2 class="bar-name">The name of the bar</h2><p class="bar-more">More details goes here</p></li>
  <li class="bar-row"><svg class="row-shape"><use href="#row-shape"/></svg><svg class="map-icon"><use href="#map-icon"/></svg><h2 class="bar-name">The name of the bar</h2><p class="bar-more">More details goes here</p></li>
  <li class="bar-row"><svg class="row-shape"><use href="#row-shape"/></svg><svg class="map-icon"><use href="#map-icon"/></svg><h2 class="bar-name">The name of the bar</h2><p class="bar-more">More details goes here</p></li>
  <li class="bar-row"><svg class="row-shape"><use href="#row-shape"/></svg><svg class="map-icon"><use href="#map-icon"/></svg><h2 class="bar-name">The name of the bar</h2><p class="bar-more">More details goes here</p></li>
  <li class="bar-row"><svg class="row-shape"><use href="#row-shape"/></svg><svg class="map-icon"><use href="#map-icon"/></svg><h2 class="bar-name">The name of the bar</h2><p class="bar-more">More details goes here</p></li>
</ul>

<div class="more-band"><div class="more-button">More ...</div></div>

<section class="contact-band">
  <h3 class="contact-title">Contact Us</h3>
  <span class="social social-one" role="img" aria-label="Social link"></span>
  <span class="social social-two" role="img" aria-label="Social link"></span>
</section>

<footer class="site-footer"></footer>
</body>
</html>
```